Need a business card design for a new business

The business is going to be called "The Maple Lectern" - it is an online training company that provides Instructor Lead training to students at any destination in the world
The reference to cloud is the internet and classroom reference will be a computer at the students and instructors end

We will need a Web site and stationary and advertising material developed over time but for now require the business cards only

So if we are happy with the business card then we will use the same designers for the other requirments of the business as it evolves

Industry/Entity Type

Advertising

```html
<!DOCTYPE html>
<html lang="en">
<head>
<meta charset="utf-8">
<title>The Maple Lectern — Business Card</title>
<link rel="stylesheet" href="https://fonts.googleapis.com/css2?family=Source+Sans+3:wght@400;600&display=swap">
<style>
  :root {
    --page-bg: #ececec;
    --card-white: #fbfbfb;
    --card-grey: #e6e6e6;
    --brand-blue: #2aa8ef;
    --ink-blue: #1f73bd;
    --text-grey: #7a7a7a;
    --card-w: 900px;
    --card-h: 514px;
  }
  * { box-sizing: border-box; margin: 0; padding: 0; }
  html, body {
    width: 1169px;
    height: 1200px;
    overflow: hidden;
    background: var(--page-bg);
    font-family: "Source Sans 3", "Helvetica Neue", Arial, sans-serif;
  }
  .sheet {
    width: 1169px;
    height: 1200px;
    display: flex;
    flex-direction: column;
    align-items: center;
    justify-content: space-evenly;
  }
  .card {
    position: relative;
    width: var(--card-w);
    height: var(--card-h);
    border-radius: 30px;
    overflow: hidden;
    box-shadow: 0 6px 18px rgba(0,0,0,0.18);
  }
  .card-shape {
    position: absolute;
    inset: 0;
    width: 100%;
    height: 100%;
  }
  .card--front { background: var(--card-white); }
  .card--back { background: var(--brand-blue); }

  .wordmark {
    position: absolute;
    left: 66px;
    top: 70px;
    display: flex;
    align-items: center;
    gap: 14px;
    color: var(--ink-blue);
    font-weight: 600;
    font-size: 48px;
    letter-spacing: -0.5px;
    line-height: 1;
  }
  .wordmark-dot {
    width: 22px;
    height: 22px;
    border-radius: 50%;
    background: var(--brand-blue);
  }

  .address {
    position: absolute;
    left: 70px;
    top: 328px;
    color: var(--text-grey);
    font-size: 21px;
    line-height: 28px;
  }
  .address .label {
    color: var(--ink-blue);
    font-weight: 600;
  }

  .holder {
    position: absolute;
    right: 70px;
    top: 280px;
    text-align: right;
  }
  .holder-name {
    color: var(--ink-blue);
    font-size: 41px;
    font-weight: 600;
    line-height: 1;
  }
  .holder-title {
    color: var(--text-grey);
    font-size: 20px;
    margin-top: 6px;
  }

  .web {
    position: absolute;
    right: 70px;
    top: 412px;
    text-align: right;
    color: var(--text-grey);
    font-size: 20px;
    line-height: 28px;
  }

  .back-brand {
    position: absolute;
    right: 66px;
    top: 340px;
    text-align: right;
  }
  .back-brand .wordmark-back {
    color: var(--ink-blue);
    font-weight: 600;
    font-size: 46px;
    letter-spacing: -0.5px;
    line-height: 1;
    white-space: nowrap;
  }
  .back-brand .back-url {
    color: var(--text-grey);
    font-size: 22px;
    margin-top: 8px;
  }
</style>
</head>
<body>
<main class="sheet">

  <section class="card card--front" aria-label="Business card front">
    <svg class="card-shape" viewBox="0 0 900 514" preserveAspectRatio="none" aria-hidden="true">
      <path d="M0 292 Q 300 318 392 514 L0 514 Z" fill="var(--card-grey)"/>
      <path d="M398 514 Q 430 168 900 128 L900 514 Z" fill="var(--card-grey)"/>
    </svg>

    <div class="wordmark">
      <span class="wordmark-dot"></span>
      <span>The Maple Lectern</span>
    </div>

    <div class="address">
      <div>2150 Harbor Lane</div>
      <div>Eastfield, OR 97512</div>
      <div><span class="label">T :</span> 1.502.614.377</div>
      <div><span class="label">F :</span> 1.502.614.378</div>
      <div><span class="label">M:</span> 1.502.930.146</div>
    </div>

    <div class="holder">
      <div class="holder-name">Your name</div>
      <div class="holder-title">Chief Executive officer</div>
    </div>

    <div class="web">
      <div>yourname@maplelectern.com</div>
      <div>www.maplelectern.com</div>
    </div>
  </section>

  <section class="card card--back" aria-label="Business card back">
    <svg class="card-shape" viewBox="0 0 900 514" preserveAspectRatio="none" aria-hidden="true">
      <path d="M0 400 Q 300 412 394 514 L0 514 Z" fill="var(--card-white)"/>
      <path d="M400 514 Q 420 150 900 104 L900 514 Z" fill="var(--card-white)"/>
    </svg>

    <div class="back-brand">
      <div class="wordmark-back">The Maple Lectern</div>
      <div class="back-url">www.maplelectern.com</div>
    </div>
  </section>

</main>
</body>
</html>
```